Business Card Design Project

Business card design with a funky, clean, modern design. Business is an immigration consultancy. Client base will be Canadian employers wanting to hire or retain foreign workers and foreign nationals wanting to immigrate to Canada.

Full color possible, but should incorporate red/white/black as per the logo to be provided. Double sided card design.

Target Market(s)

Canadian employers looking to hire/retain staff and also foreign nationals immigrating to Canada

Industry/Entity Type

Business

Requirements
Must have
• Logo (to be provided)
Name (Marla Voskuil, Immigration Consultant)
Phone (604) 731-5562
E-mail: marla@tallowbrookmigration.example
Web: www.tallowbrookmigration.example

Nice to have
• Tag Line
Clean, modern style

```html
<!DOCTYPE html>
<html lang="en">
<head>
<meta charset="utf-8">
<title>Tallowbrook Migration — Business Card</title>
<link href="https://fonts.googleapis.com/css2?family=Roboto:wght@300;400;700&display=swap" rel="stylesheet">
<style>
  :root {
    --canvas: #d9d9d9;
    --card-black: #0b0b0b;
    --card-white: #ffffff;
    --brand-red: #d01616;
    --ink: #222222;
    --ink-soft: #444444;
    --text-white: #ffffff;
  }
  html, body {
    margin: 0;
    padding: 0;
    width: 1200px;
    height: 900px;
    overflow: hidden;
    background: var(--canvas);
    font-family: "Roboto", Arial, sans-serif;
  }
  .canvas {
    width: 1200px;
    height: 900px;
    display: flex;
    align-items: center;
    justify-content: center;
    gap: 40px;
  }
  .card {
    position: relative;
    width: 520px;
    height: 297px;
    overflow: hidden;
    box-shadow: 0 6px 18px rgba(0,0,0,0.25);
  }

  /* Front side */
  .card--front {
    background: var(--card-black);
    display: flex;
    align-items: center;
    justify-content: center;
  }
  .brand {
    display: flex;
    align-items: center;
    gap: 12px;
  }
  .brand__dot {
    width: 22px;
    height: 22px;
    border-radius: 50%;
    background: var(--brand-red);
    flex: none;
  }
  .brand__name {
    font-weight: 700;
    letter-spacing: 2px;
    text-transform: uppercase;
    line-height: 1.05;
  }
  .card--front .brand__name {
    color: var(--text-white);
    font-size: 26px;
  }

  /* Back side */
  .card--back {
    background: var(--card-white);
  }
  .card--back .brand {
    position: absolute;
    left: 34px;
    top: 42px;
  }
  .card--back .brand__dot {
    width: 16px;
    height: 16px;
  }
  .card--back .brand__name {
    color: var(--ink);
    font-size: 16px;
    letter-spacing: 1.5px;
  }
  .holder {
    position: absolute;
    right: 40px;
    top: 34px;
    text-align: right;
    color: var(--ink);
  }
  .holder__name {
    font-size: 17px;
    font-weight: 400;
  }
  .holder__title {
    font-size: 10px;
    color: var(--ink-soft);
    letter-spacing: 0.5px;
  }
  .corner-tab {
    position: absolute;
    right: 0;
    top: 30px;
  }
  .contact {
    position: absolute;
    left: 34px;
    bottom: 44px;
    list-style: none;
    margin: 0;
    padding: 0;
    color: var(--ink);
    font-size: 13px;
    font-weight: 300;
    line-height: 1.45;
  }
  .contact__item {
    display: flex;
    align-items: center;
    gap: 8px;
  }
  .contact__item svg { flex: none; }
  .edge-band {
    position: absolute;
    left: 0;
    right: 0;
    bottom: 0;
    height: 9px;
    background: var(--brand-red);
  }
  .edge-bar {
    position: absolute;
    right: 0;
    bottom: 9px;
    width: 12px;
    height: 150px;
    background: var(--card-black);
  }
</style>
</head>
<body>
<main class="canvas">
  <section class="card card--front" aria-label="Card front">
    <div class="brand">
      <span class="brand__dot"></span>
      <span class="brand__name">Tallowbrook<br>Migration</span>
    </div>
  </section>

  <section class="card card--back" aria-label="Card back">
    <div class="brand">
      <span class="brand__dot"></span>
      <span class="brand__name">Tallowbrook<br>Migration</span>
    </div>

    <div class="holder">
      <div class="holder__name">Marla Voskuil</div>
      <div class="holder__title">RCIC</div>
    </div>
    <svg class="corner-tab" width="18" height="26" viewBox="0 0 18 26" aria-hidden="true">
      <polygon points="18,0 0,13 18,26" fill="var(--brand-red)"/>
    </svg>

    <ul class="contact">
      <li class="contact__item">
        <svg width="9" height="9" viewBox="0 0 9 9" aria-hidden="true"><rect x="2" y="0.5" width="5" height="8" rx="1" fill="none" stroke="var(--brand-red)" stroke-width="1.2"/></svg>
        (604) 731-5562
      </li>
      <li class="contact__item">
        <svg width="9" height="9" viewBox="0 0 9 9" aria-hidden="true"><rect x="0.6" y="1.6" width="7.8" height="5.8" fill="none" stroke="var(--brand-red)" stroke-width="1.2"/><polyline points="0.6,1.6 4.5,5 8.4,1.6" fill="none" stroke="var(--brand-red)" stroke-width="1"/></svg>
        marla@tallowbrookmigration.example
      </li>
      <li class="contact__item">
        <svg width="9" height="9" viewBox="0 0 9 9" aria-hidden="true"><circle cx="4.5" cy="4.5" r="3.8" fill="none" stroke="var(--brand-red)" stroke-width="1.2"/><line x1="0.7" y1="4.5" x2="8.3" y2="4.5" stroke="var(--brand-red)" stroke-width="1"/></svg>
        www.tallowbrookmigration.example
      </li>
    </ul>

    <div class="edge-bar"></div>
    <div class="edge-band"></div>
  </section>
</main>
</body>
</html>
```